(Wix) Website Design Tweaks

The site: www.MarbleFinchCo.com
(The coding must be done within Wix. I will create a duplicate website so you can gain access and begin editing.)

My website contains my preferred text and images - but it needs to look more professional. My business focuses on "Corporate Messaging" and "Marketing Communications", so the website needs to look professional, but not too corporate. My clients range from very big companies to technology startups - the look and feel should be uncluttered, professional, and modern.

I want someone to review the pages, and make changes / suggestions focused on:
1) Fonts
2) Colors
3) Layout

If you have ideas for adding additional graphics, that's fine, but they should be consistent with what I already have . . . unless you think some / all of my images need to be changed.

My site is very, very small, and only contains 5 (very short) pages. There are no sub-pages. (One page is the contact page, with almost nothing except form fields.)

If you do a good job with my site, I may be able to provide you with additional work - many of my clients need website design tweaks, after I provide the verbiage.

```html
<!DOCTYPE html>
<html lang="en">
<head>
<meta charset="utf-8">
<title>Marble Finch — Inform. Influence. Sell.</title>
<link rel="stylesheet" href="https://fonts.googleapis.com/css2?family=Poppins:wght@600;700;800&family=Roboto:wght@400;500;700&display=swap">
<style>
:root{
  --blue:#0aa6ec;
  --blue-deep:#0b86d6;
  --navy:#061a3a;
  --ink:#0b0b0b;
  --body:#6b6b6b;
  --white:#ffffff;
  --footer:#0a0a0a;
}
*{box-sizing:border-box;margin:0;padding:0}
html,body{width:1200px;height:3294px;overflow:hidden}
body{position:relative;background:var(--white);font-family:"Roboto",Arial,sans-serif;color:var(--body)}
.abs{position:absolute}

/* hero */
.hero{left:0;top:0;width:1200px;height:642px;
  background:radial-gradient(circle at 836px 316px,#bfe8ff 0,#3aa8f0 40px,#0d5bb5 120px,#0a3f8c 230px,#072a5e 420px,#041736 700px)}
.logo{left:111px;top:31px;width:69px;height:69px;background:var(--blue);color:var(--white);
  font-size:12px;line-height:13px;padding:38px 4px 0 5px;text-transform:uppercase}
.nav{left:407px;top:56px;display:flex;gap:34px;font-weight:700;font-size:15px;color:var(--white)}
.nav .active{color:var(--blue)}
.btn{display:flex;align-items:center;justify-content:center;background:var(--blue);color:var(--white);
  font-weight:700;font-size:16px;text-transform:uppercase}
.nav-cta{left:952px;top:46px;width:136px;height:40px}
.hero-title{left:110px;top:250px;font-family:"Poppins",sans-serif;font-weight:800;font-size:35px;color:var(--white);letter-spacing:-.3px}
.hero-text{left:112px;top:313px;width:480px;font-size:17px;line-height:28px;font-weight:500;color:var(--white)}
.hero-cta{left:113px;top:391px;width:165px;height:52px}

/* feature rows */
.frame{background:var(--blue)}
.h2{font-family:"Poppins",sans-serif;font-weight:800;font-size:40px;color:var(--ink);letter-spacing:-.3px;text-transform:uppercase}
.copy{font-size:14.5px;line-height:25px;text-align:justify}
.copy p+p{margin-top:12px}
.learn{width:165px;height:47px}

/* expertise */
.expertise{left:0;top:2252px;width:1200px;height:671px;
  background:linear-gradient(120deg,#0d9de8 0%,#12aef2 45%,#0a94e0 100%)}
.exp-title{left:147px;top:2313px;font-family:"Poppins",sans-serif;font-weight:700;font-size:34px;color:var(--white)}
.exp-text{left:148px;top:2370px;width:634px;font-size:14.5px;line-height:25px;color:var(--white);text-align:justify}
.view-all{left:889px;top:2359px;width:176px;height:43px;background:var(--white);color:var(--blue);font-size:13px}
.card{width:219px;height:174px;background:var(--white);display:flex;flex-direction:column;align-items:center;justify-content:center;
  gap:12px;color:var(--ink);font-weight:500;font-size:17px;line-height:24px;text-align:center}
.card svg{width:76px;height:76px;stroke:var(--blue);fill:none;stroke-width:2.4;stroke-linecap:round;stroke-linejoin:round}

/* clients */
.clients-title{left:0;top:3005px;width:1200px;text-align:center;font-family:"Poppins",sans-serif;font-weight:700;font-size:35px;color:var(--ink)}
.client{top:3097px;width:140px;height:60px;display:flex;align-items:center;justify-content:center;gap:8px;
  font-family:"Roboto",sans-serif;font-weight:700;font-size:15px;color:#3a3a3a;white-space:nowrap}
.client .dot{width:14px;height:14px;border-radius:50%;background:#7a7a7a;flex:none}

.footer{left:0;top:3239px;width:1200px;height:55px;background:var(--footer);color:var(--white);
  display:flex;align-items:center;justify-content:center;font-size:14px;gap:14px}
</style>
</head>
<body>

<div class="abs hero" role="img" aria-label="Glowing blue particle vortex with white paper planes flying across it"></div>
<div class="abs logo">Marble &amp;<br>Finch</div>
<nav class="abs nav"><span class="active">HOME</span><span>PITCH CAMP</span><span>TESTIMONIALS</span><span>TEAM</span><span>CONTACT</span></nav>
<div class="abs btn nav-cta">Get Started</div>
<h1 class="abs hero-title">INFORM. INFLUENCE. SELL.</h1>
<p class="abs hero-text">Sed ut perspiciatis unde omnis iste natus error sit voluptatem accusantium doloremque laudantium</p>
<div class="abs btn hero-cta">Get Started</div>

<!-- challenge -->
<div class="abs frame" style="left:95px;top:855px;width:371px;height:307px"></div>
<div class="abs" style="left:111px;top:757px;width:447px;height:388px;background:linear-gradient(135deg,#cfe3f2,#7fb4da 55%,#2f6fa8)" role="img" aria-label="Hand holding a tablet beneath floating cloud and device icons"></div>
<h2 class="abs h2" style="left:635px;top:773px">The Big Challenge</h2>
<div class="abs copy" style="left:636px;top:848px;width:427px">
<p>In today’s competitive business environment, effective communication is more essential than ever before. It is the foundation upon which companies are built, careers are propelled, and knowledge is imparted.</p>
<p>Effective communication is critical - without it, misunderstandings arise, errors occur, and business goals are frustrated. In short, effective communication is the key driver</p>
</div>
<div class="abs btn learn" style="left:636px;top:1071px">Learn More</div>

<!-- help -->
<h2 class="abs h2" style="left:111px;top:1293px">How We Help</h2>
<div class="abs copy" style="left:111px;top:1367px;width:428px">
<p>At Marble Finch, we help individuals and organizations “get what they want” through clear and persuasive communication. Our consulting, coaching, and training services help clients achieve targeted business objectives, with an emphasis on informing, influencing, and selling.</p>
</div>
<div class="abs btn learn" style="left:113px;top:1529px">Learn More</div>
<div class="abs frame" style="left:733px;top:1343px;width:371px;height:307px"></div>
<div class="abs" style="left:640px;top:1246px;width:447px;height:387px;background:radial-gradient(circle at 62% 45%,#9fd9f2,#2a7fb0 30%,#0c3a5a 65%,#061d30)" role="img" aria-label="Digital globe surrounded by network of people icons touched by a fingertip"></div>

<!-- results -->
<div class="abs frame" style="left:95px;top:1832px;width:371px;height:306px"></div>
<div class="abs" style="left:111px;top:1735px;width:447px;height:387px;background:radial-gradient(circle at 50% 50%,#f4d7b8,#6a5a9a 18%,#1c2a6e 50%,#0a1238)" role="img" aria-label="Two hands reaching toward a glowing sphere ringed by communication icons"></div>
<h2 class="abs h2" style="left:635px;top:1794px">Results</h2>
<div class="abs copy" style="left:636px;top:1868px;width:427px">
<p>Whatever the message, and whatever the medium, we help clients establish a connection, make an impression, and drive audiences toward a predetermined course of action. This results in clear messaging, captivated audiences, and increased sales.</p>
</div>
<div class="abs btn learn" style="left:636px;top:2005px">Learn More</div>

<!-- expertise -->
<section class="abs expertise"></section>
<h2 class="abs exp-title">EXPERTISE</h2>
<p class="abs exp-text">Sed ut perspiciatis unde omnis iste natus error sit voluptatem accusantium doloremque laudantium, totam rem aperiam, eaque ipsa quae ab illo inventore veritatis et quasi architecto beatae vitae dicta sunt explicabo.</p>
<div class="abs btn view-all">View All Expertise</div>

<div class="abs card" style="left:136px;top:2482px"><svg viewBox="0 0 76 76"><rect x="26" y="8" width="42" height="28"/><polyline points="32,28 40,20 48,25 58,14"/><circle cx="16" cy="12" r="5"/><path d="M10 22h12v24H10z"/><path d="M40 36v8"/><circle cx="36" cy="52" r="4"/><circle cx="52" cy="52" r="4"/><path d="M29 66c0-5 3-8 7-8s7 3 7 8M45 66c0-5 3-8 7-8s7 3 7 8"/></svg>Sales Training</div>
<div class="abs card" style="left:372px;top:2482px"><svg viewBox="0 0 76 76"><rect x="24" y="6" width="46" height="30"/><circle cx="40" cy="22" r="7"/><path d="M40 15v7h7"/><path d="M54 30v-6M58 30v-10M62 30v-14"/><circle cx="14" cy="12" r="5"/><path d="M8 22h12v30H8z"/><circle cx="44" cy="48" r="5"/><circle cx="60" cy="48" r="5"/><path d="M36 66c0-6 4-9 8-9s8 3 8 9M52 66c0-6 4-9 8-9s8 3 8 9"/></svg>Presentation Skills<br>Training</div>
<div class="abs card" style="left:609px;top:2482px"><svg viewBox="0 0 76 76"><ellipse cx="44" cy="18" rx="18" ry="11"/><path d="M36 22h16M36 16h16"/><circle cx="22" cy="40" r="7"/><circle cx="54" cy="40" r="7"/><path d="M8 68c0-9 6-14 14-14s14 5 14 14zM40 68c0-9 6-14 14-14s14 5 14 14z"/></svg>Keystone Talks</div>
<div class="abs card" style="left:847px;top:2482px"><svg viewBox="0 0 76 76"><rect x="14" y="12" width="48" height="58"/><path d="M38 12v58"/><path d="M28 4h20v8H28z"/><path d="M26 34v-10l-4 4M26 24l4 4M50 24v10l-4-4M50 34l4-4"/></svg>Elevator Pitches</div>

<div class="abs card" style="left:136px;top:2675px"><svg viewBox="0 0 76 76"><circle cx="38" cy="16" r="9"/><path d="M24 44c0-10 6-16 14-16s14 6 14 16"/><path d="M16 44h44v6H16z"/><path d="M26 50h24l-3 20H29z"/></svg>Keynote Speeches</div>
<div class="abs card" style="left:372px;top:2675px"><svg viewBox="0 0 76 76"><rect x="12" y="20" width="46" height="34"/><path d="M6 60h58v4H6z"/><rect x="18" y="26" width="16" height="12"/><path d="M38 28h14M38 34h14M18 44h34"/><path d="M54 8l10 4v10c0 6-4 10-10 12-6-2-10-6-10-12V12z"/><polyline points="50,20 53,23 58,17"/></svg>Marketing Collateral</div>
<div class="abs card" style="left:609px;top:2675px"><svg viewBox="0 0 76 76"><rect x="6" y="6" width="52" height="34"/><path d="M12 14h30M12 22h22M12 30h18"/><circle cx="52" cy="40" r="7"/><path d="M40 70V56c0-5 5-8 12-8s12 3 12 8v14"/><path d="M42 52l-10-6"/></svg>Business Presentations<br>&amp; Decks</div>
<div class="abs card" style="left:847px;top:2675px"><svg viewBox="0 0 76 76"><path d="M10 10h18M10 16h18M10 22h18"/><circle cx="54" cy="18" r="12"/><path d="M54 11v14M58 14h-6a2 2 0 0 0 0 4h4a2 2 0 0 1 0 4h-6"/><path d="M8 66h60"/><path d="M12 66V50h6v16M22 66V44h6v22M32 66V52h6v14"/><path d="M10 44l10-8 8 4 12-10"/><rect x="44" y="40" width="20" height="26"/></svg>Venture Capital<br>Presentations &amp; Decks</div>

<!-- clients -->
<h2 class="abs clients-title">OUR CLIENTS</h2>
<div class="abs client" style="left:92px"><span class="dot" style="border-radius:2px"></span>Lumenpath</div>
<div class="abs client" style="left:240px">Tessaro</div>
<div class="abs client" style="left:387px">Brightwell</div>
<div class="abs client" style="left:535px"><span class="dot"></span>Westbrook</div>
<div class="abs client" style="left:682px"><span class="dot"></span>Aurelian</div>
<div class="abs client" style="left:830px">Harbor City Bar</div>
<div class="abs client" style="left:978px">Corvane Oncology</div>

<footer class="abs footer"><span>© 2022 marblefinchco</span><span>|</span><span>All Rights Reserved</span><span>|</span><span>Terms and Conditions</span></footer>

</body>
</html>
```